Magento e-commerce webdesign

We need a full e-commerce design for a company based in France. The website will sell belts (men / women).
In files, you have our logo. We made a try for a brown visit card, but it's just an idea. The brown color can be used if it looks like leather, warning it MUSN'T look like "brown shit" :)
So you are free with color but never forget we sell belts and it's both for men & women (upmarket). You can make your own colors changes on the logo (only colors).
You'll find 2 wireframes with the home page & the category page. Elements are in french. UPDATED : you have a traduction files, but it would better if you can make it in french.
Photos have to be on a white background.
Carroussel & every pictures of the wireframes area are very importants.
Target Market(s)
Men & women
Fashion peoples
Upmarket
Industry/Entity Type
It Company
Requirements
Must have
- work on the colors
- work on the pictures (carroussel, newsletter, ventes privées, services, category)
- pro & upmarket
Nice to have
- Product detail page
- Texts in french
Should not have
- Shitty brown colors

```html
<!DOCTYPE html>
<html lang="fr">
<head>
<meta charset="utf-8">
<title>Sanglea – Ceintures</title>
<link href="https://fonts.googleapis.com/css2?family=Arimo:wght@400;700&family=Gelasio:ital,wght@0,400;1,400;1,700&display=swap" rel="stylesheet">
<style>
:root{
  --ink:#2b2b2b;
  --header-dark:#1c1a19;
  --header-mid:#2a2725;
  --leather:#5b3f30;
  --nav-band:#8d7f6c;
  --nav-active:#3a2a20;
  --plum:#6a1c44;
  --plum-deep:#2e1a1f;
  --pink:#e2439a;
  --button:#5e1a3c;
  --line:#e4e4e4;
  --box-line:#cfcfcf;
  --social-1:#8d7c68;
  --social-2:#8b5d3c;
  --social-3:#4b3022;
  --footer:#1e1c1b;
  --white:#ffffff;
}
*{margin:0;padding:0;box-sizing:border-box}
html,body{width:1200px;height:1199px;overflow:hidden;background:var(--white)}
body{position:relative;font-family:"Arimo",Arial,sans-serif;color:var(--ink);font-size:12px}
.abs{position:absolute}
.serif{font-family:"Gelasio",Georgia,serif}

.site-header{left:0;top:0;width:1200px;height:147px;background:linear-gradient(var(--header-dark) 0 37px,var(--header-mid) 37px 147px)}
.brand{left:80px;top:0;width:224px;height:111px;background:var(--leather);display:flex;align-items:center;justify-content:center;gap:10px}
.brand-dot{width:14px;height:14px;border-radius:50%;background:#efe6dc}
.brand-name{font-family:"Gelasio",Georgia,serif;font-size:36px;color:#efe6dc}
.brand-url{left:80px;top:120px;width:224px;text-align:center;color:#8a7c6d;font-size:12px;letter-spacing:2px}
.basket{left:780px;top:68px;width:334px;height:33px;background:var(--white);border-radius:17px;display:flex;align-items:center;padding-left:62px;font-family:"Gelasio",Georgia,serif;font-size:13px;color:#555;gap:14px}
.basket-icon{left:778px;top:60px;width:48px;height:48px;border-radius:50%;background:var(--leather);border:3px solid var(--white)}

.main-nav{left:0;top:147px;width:1200px;height:37px;background:var(--nav-band)}
.nav-item{top:147px;height:37px;line-height:37px;color:var(--white);font-size:14px;text-align:center}

.breadcrumb{left:80px;top:196px;font-size:10px}

.hero{left:80px;top:219px;width:731px;height:353px;background:linear-gradient(100deg,#6a6a6a 0%,#3a3a3a 28%,#0c0c0c 55%,#000 100%)}
.hero-title{right:20px;top:185px;color:var(--white);font-size:38px;text-align:right;line-height:1.1}
.hero-sub{right:20px;top:238px;color:var(--white);font-size:28px}
.hero-dots{right:20px;bottom:18px;display:flex;gap:5px}
.hero-dots span{width:15px;height:15px;border-radius:50%;border:2px solid #d9c9b4;background:#6a5848}
.hero-dots span:first-child{background:#a89579}

.signup-title{left:824px;top:220px;color:var(--pink);font-size:21px;text-decoration:underline;letter-spacing:1px}
.signup-text{left:824px;top:256px;font-size:11px;line-height:17px;width:200px}
.signup-form{left:824px;top:300px;width:272px;height:24px;border:1px solid #b9b0a6;border-radius:12px;font-size:10.5px;padding-left:11px;line-height:22px;color:#555}
.signup-btn{right:-1px;top:-1px;width:64px;height:24px;border-radius:12px;background:var(--leather);color:var(--white);text-align:center;line-height:24px}
.promo{left:824px;top:337px;width:290px;height:110px;background:linear-gradient(90deg,#5a1734,#7a2a4e 60%,#5a1734)}
.promo-burst{left:12px;top:14px;width:80px;height:80px;border-radius:50%;background:var(--pink);color:var(--white);text-align:center;font-style:italic;font-weight:700}
.promo-label{right:12px;bottom:4px;color:var(--white);font-size:23px;font-style:italic}
.services{left:824px;top:460px;width:290px;height:112px}
.svc-tag{background:#333;color:#ddd;font-size:18px;line-height:20px;padding:0 5px;letter-spacing:.5px}
.svc-pink{color:#e96ab0}
.svc-photo{left:110px;top:25px;width:180px;height:60px;border-radius:30px;background:linear-gradient(90deg,#b5ab95,#8f8571)}

.product{top:614px;width:202px}
.product-photo{height:104px;background:radial-gradient(ellipse at center,#3b3b3b 0 28%,#f4f4f4 60%,#fff 75%)}
.product-rule{height:3px;background:var(--line);margin-top:11px}
.product-name{margin:13px 4px 0;font-size:12px;line-height:15px;color:#444}
.product-price{margin:17px 4px 0;font-size:11px;color:#444}
.details{display:inline-block;margin-top:6px;width:90px;height:24px;line-height:24px;text-align:center;color:var(--white);background:var(--button);border-radius:4px;font-size:12px}

.info-box{top:885px;height:96px;border:1px solid var(--box-line);border-radius:7px}
.info-head{position:absolute;left:11px;right:11px;top:6px;height:30px;border-bottom:1px solid var(--line);display:flex;align-items:center;gap:10px;font-family:"Gelasio",Georgia,serif;font-style:italic;font-weight:700;font-size:13px;color:#333}
.info-body{position:absolute;left:0;right:0;top:48px;text-align:center;font-size:11px;line-height:16px;color:#444}
.card{display:inline-block;width:44px;height:27px;border-radius:3px;margin:0 2px}

.social{top:1025px;height:78px;border-radius:3px;color:var(--white);font-family:"Gelasio",Georgia,serif;font-style:italic;font-weight:700;font-size:18px}
.social-bubble{position:absolute;left:16px;top:12px;width:62px;height:52px;border-radius:50%;background:rgba(255,255,255,.25)}
.social-text{position:absolute;right:22px;top:27px}

.site-footer{left:0;top:1140px;width:1200px;height:59px;background:var(--footer);color:var(--white);font-size:12px}
</style>
</head>
<body>

<header class="abs site-header"></header>
<div class="abs brand"><span class="brand-dot"></span><span class="brand-name">sanglea</span></div>
<div class="abs brand-url">www.sanglea.com</div>
<div class="abs basket"><span>0,00 $</span><span>|</span><span>Shopping Basket</span><span>|</span><span>Checkout</span></div>
<div class="abs basket-icon"><svg width="42" height="42" viewBox="0 0 42 42"><path d="M12 19h18l-2 9H14z" fill="none" stroke="#fff" stroke-width="2"/><path d="M15 19l3-5M27 19l-3-5" stroke="#fff" stroke-width="2"/></svg></div>

<nav>
  <div class="abs main-nav"></div>
  <div class="abs nav-item" style="left:80px;width:96px;background:var(--nav-active)">HOMME</div>
  <div class="abs nav-item" style="left:196px;width:92px">FEMME</div>
  <div class="abs nav-item" style="left:318px;width:118px">ACCESSOIRES</div>
  <div class="abs nav-item" style="left:881px;width:116px;background:var(--plum)">MON COMPTE</div>
  <div class="abs nav-item" style="left:997px;width:117px;background:var(--plum-deep)">PARRAINAGE</div>
</nav>

<div class="abs breadcrumb">Home</div>

<section class="abs hero" role="img" aria-label="Photo d'un homme en tenue noire portant une ceinture">
  <div class="abs hero-title serif">Les nouvelles collections</div>
  <div class="abs hero-sub serif">deja chez sanglea.com!</div>
  <div class="abs hero-dots"><span></span><span></span><span></span><span></span><span></span></div>
</section>

<aside>
  <div class="abs signup-title serif">EAIL SIGN U P</div>
  <div class="abs signup-text">To receive our exclusive offers and latest product news!</div>
  <div class="abs signup-form">Enter your email<span class="abs signup-btn">Signup</span></div>
  <div class="abs promo" role="img" aria-label="Bannière ventes privées avec arbre décoratif">
    <div class="abs promo-burst"><div style="margin-top:20px;font-size:13px;text-decoration:line-through">-25%</div><div style="font-size:21px">-50%</div></div>
    <div class="abs promo-label serif">Vente Prives</div>
  </div>
  <div class="abs services">
    <div class="abs svc-photo" role="img" aria-label="Ceinture tressée beige"></div>
    <div style="position:relative">
      <span class="svc-tag" style="display:inline-block">TO RECIVESY</span><br>
      <span class="svc-tag" style="display:inline-block">SERVICES</span><br>
      <span class="svc-tag" style="display:inline-block;padding-right:40px">COLLECTIONS</span><br>
      <span class="svc-tag svc-pink" style="display:inline-block;margin-top:6px">SERVICES</span><br>
      <span class="svc-tag svc-pink" style="display:inline-block;padding-right:40px">COLLECTIONS</span>
    </div>
  </div>
</aside>

<main>
  <article class="abs product" style="left:80px">
    <div class="product-photo" role="img" aria-label="Ceinture en cuir noir" style="border:1px solid var(--line)"></div>
    <div class="product-rule"></div>
    <p class="product-name">Ceinture Réversible et Ajustable boucle Ligne Claire</p>
    <p class="product-price">78 $</p>
    <span class="details">Details</span>
  </article>
  <article class="abs product" style="left:355px">
    <div class="product-photo" role="img" aria-label="Ceinture tressée beige" style="background:radial-gradient(ellipse at center,#9a907c 0 28%,#f4f4f4 60%,#fff 75%)"></div>
    <div class="product-rule"></div>
    <p class="product-name">Ceinture Réversible et Ajustable boucle Ligne Claire</p>
    <p class="product-price">78 $</p>
    <span class="details">Details</span>
  </article>
  <article class="abs product" style="left:647px">
    <div class="product-photo" role="img" aria-label="Ceinture en cuir blanc" style="background:radial-gradient(ellipse at center,#dcdcdc 0 28%,#f6f6f6 60%,#fff 75%)"></div>
    <div class="product-rule"></div>
    <p class="product-name">Ceinture Réversible et Ajustable boucle Ligne Claire</p>
    <p class="product-price">78 $</p>
    <span class="details">Details</span>
  </article>
  <article class="abs product" style="left:912px">
    <div class="product-photo" role="img" aria-label="Ceinture en cuir noir à boucle plaque"></div>
    <div class="product-rule"></div>
    <p class="product-name">Ceinture Réversible et Ajustable boucle Ligne Claire</p>
    <p class="product-price">78 $</p>
    <span class="details">Details</span>
  </article>

  <section class="abs info-box" style="left:80px;width:240px">
    <div class="info-head"><svg width="20" height="24"><rect x="2" y="10" width="16" height="13" fill="#222"/><path d="M5 10V6a5 5 0 0 1 10 0v4" fill="none" stroke="#222" stroke-width="3"/></svg>Paiement CB + portefeuille</div>
    <div class="info-body" style="top:48px"><span class="card" style="background:#f2a81d"></span><span class="card" style="background:#c8102e"></span><span class="card" style="background:#d8dfe8;border:1px solid #aaa"></span><span class="card" style="background:#eee;border:1px solid #aaa"></span></div>
  </section>
  <section class="abs info-box" style="left:341px;width:240px">
    <div class="info-head"><svg width="32" height="22"><rect x="1" y="3" width="18" height="13" fill="#333"/><path d="M19 7h7l5 5v4H19z" fill="#333"/><circle cx="7" cy="18" r="3" fill="#333"/><circle cx="25" cy="18" r="3" fill="#333"/></svg>Livraison</div>
    <div class="info-body" style="top:56px">Votre commande expédiée sous 24h</div>
  </section>
  <section class="abs info-box" style="left:609px;width:240px">
    <div class="info-head"><svg width="30" height="22"><path d="M4 3c6-3 12 0 14 4l-3 3c3 4 6 6 10 7l2-3c4 2 2 7-1 8C14 23 3 12 4 3z" fill="#333"/></svg>Service client</div>
    <div class="info-body" style="top:46px"><div style="margin:0 auto;width:146px;height:22px;border:1px solid #bbb;border-radius:11px;position:relative;line-height:20px;padding-left:56px;text-align:left"><span style="position:absolute;left:0;top:0;width:50px;height:20px;border-radius:10px;background:#999"></span>06 000 123 45</div><div style="margin-top:3px">Service client téléphone et email</div></div>
  </section>
  <section class="abs info-box" style="left:874px;width:240px">
    <div class="info-head"><svg width="20" height="24"><circle cx="10" cy="7" r="5" fill="#222"/><path d="M2 23c0-8 16-8 16 0z" fill="#222"/></svg>Garantie</div>
    <div class="info-body" style="top:50px">Garantie 10 jours "Satisfait<br>ou Remboursé"</div>
  </section>

  <a class="abs social" style="left:80px;width:337px;background:var(--social-1)"><span class="social-bubble"></span><span class="social-text">Derniers articles du blog</span></a>
  <a class="abs social" style="left:433px;width:336px;background:var(--social-2)"><span class="social-bubble"></span><span class="social-text">Fil social 683 followers</span></a>
  <a class="abs social" style="left:785px;width:336px;background:var(--social-3)"><span class="social-bubble"></span><span class="social-text">Page amis 6715 fans</span></a>
</main>

<footer class="abs site-footer">
  <div class="abs" style="left:107px;top:22px">CGV &nbsp;&nbsp;&nbsp;|&nbsp;&nbsp; CGU &nbsp;&nbsp;&nbsp;|&nbsp;&nbsp;&nbsp; Plan du site</div>
  <div class="abs" style="left:849px;top:25px">© Sanglea &nbsp;&nbsp;&nbsp;&nbsp; Contact Us &nbsp;&nbsp;&nbsp;&nbsp; Privacy Policy</div>
</footer>

</body>
</html>
```